Tellowra Sound Carnival Poster

We need a music festival design that is bright, colourful & vibrant. Space for 28-32 band names & info - Tellowra Sound Carnival, 20th July, Tickets & Info tellowrasoundcarnival-demo.com, Attached are other poster for inspo. Family festival that has Blues, Roots, Folk, Reggae, Rock, Country please see design encapsulates that. Original logo colours would be desirable.

Target Market(s)

30-55 male and females and children under 18

Colors
f04a50
ec1f27
f37122
3176b5
fbed22
ffffff
000000
959595

Requirements
Must have
• Would be great to have colour and also have the background of the poster reflect our landscape. Big escarpment surrounding a small village that you travel through narrow winding roads (think the back roads of England) over undulating green rolling hills and big blue sky. It would hurt to have kookaburras or galahs (Australian birds) flying through the air or sitting in the trees.

```html
<!DOCTYPE html>
<html lang="en">
<head>
<meta charset="utf-8">
<title>Tellowra Sound Carnival</title>
<link rel="stylesheet" href="https://fonts.googleapis.com/css2?family=Passion+One:wght@700&family=Dosis:wght@500&family=Gochi+Hand&family=Roboto:wght@700&display=swap">
<style>
  :root {
    --coral: #f04a50;
    --red: #ec1f27;
    --orange: #f37122;
    --blue: #3176b5;
    --yellow: #fbed22;
    --white: #ffffff;
    --black: #000000;
    --grey: #959595;
  }
  * { margin: 0; padding: 0; box-sizing: border-box; }
  html, body { width: 782px; height: 1200px; overflow: hidden; background: var(--white); }
  .poster { position: relative; width: 782px; height: 1200px; overflow: hidden; }

  .backdrop {
    position: absolute; left: 0; top: 0; width: 782px; height: 1136px;
    background:
      radial-gradient(ellipse at 20% 30%, var(--orange) 0%, transparent 45%),
      radial-gradient(ellipse at 85% 55%, var(--yellow) 0%, transparent 40%),
      radial-gradient(ellipse at 10% 80%, var(--blue) 0%, transparent 35%),
      linear-gradient(160deg, var(--yellow) 0%, var(--orange) 30%, var(--coral) 55%, var(--yellow) 80%, var(--blue) 100%);
  }

  .frame {
    position: absolute; left: 64px; top: 32px; width: 672px; height: 820px;
    border: 30px solid var(--red); border-radius: 28px;
  }

  .masthead {
    position: absolute; left: 90px; top: 52px; width: 620px; height: 256px;
    background: var(--black); border-radius: 14px;
    text-align: center; color: var(--white);
  }
  .masthead__name {
    font-family: "Passion One", sans-serif; font-weight: 700;
    font-size: 96px; line-height: 1; letter-spacing: 1px;
    margin-top: 30px;
    -webkit-text-stroke: 3px var(--red);
    paint-order: stroke fill;
  }
  .masthead__sub {
    font-family: "Passion One", sans-serif; font-weight: 700;
    font-size: 46px; line-height: 1; margin-top: 26px;
    -webkit-text-stroke: 3px var(--red);
    paint-order: stroke fill;
  }

  .lineup {
    position: absolute; left: 148px; top: 336px; width: 476px; height: 490px;
    background: var(--white);
    box-shadow: 10px 10px 0 var(--grey);
    padding-top: 10px;
    font-family: "Dosis", sans-serif; font-weight: 500;
    font-size: 24px; line-height: 39.4px; color: var(--black);
    text-align: center;
  }
  .lineup p { white-space: nowrap; }

  .guitar {
    position: absolute; left: 70px; top: 842px; width: 160px; height: 150px;
    border-radius: 45% 45% 50% 50%;
    background: radial-gradient(ellipse at 50% 60%, var(--yellow) 0%, var(--orange) 60%, var(--blue) 100%);
  }

  .date-badge {
    position: absolute; left: 508px; top: 784px; width: 240px; height: 240px;
    border-radius: 50%; background: var(--black);
    border: 12px solid var(--orange);
    display: flex; flex-direction: column; align-items: center; justify-content: center;
    font-family: "Gochi Hand", cursive; font-size: 50px; line-height: 48px;
    color: var(--white); -webkit-text-stroke: 2px var(--orange); paint-order: stroke fill;
  }

  .ticket-band {
    position: absolute; left: 150px; top: 1040px; width: 500px; height: 96px;
    background: var(--white); border-radius: 60px 60px 0 0;
  }
  .tickets {
    position: absolute; left: 0; top: 1064px; width: 782px; text-align: center;
    font-family: "Roboto", sans-serif; font-weight: 700; font-size: 26px; line-height: 32px;
    color: var(--black);
  }

  .sponsors {
    position: absolute; left: 0; top: 1136px; width: 782px; height: 64px;
    background: var(--white); text-align: center;
    font-family: "Roboto", sans-serif; font-weight: 700; font-size: 26px; line-height: 64px;
    color: var(--black);
  }
</style>
</head>
<body>
<div class="poster">
  <div class="backdrop" role="img" aria-label="Swirling ribbons of red, orange, yellow and blue flowing across the poster"></div>
  <div class="frame"></div>

  <header class="masthead">
    <h1 class="masthead__name">TELLOWRA</h1>
    <h2 class="masthead__sub">SOUND CARNIVAL</h2>
  </header>

  <section class="lineup" aria-label="Lineup">
    <p>ANDTYUER - ATRETTYUIO -</p>
    <p>QOOREIDSEUUA- AAAAAAA - AAAAAAA -</p>
    <p>AAAAAAA - AAAAAAA - AAAAAAA -</p>
    <p>AAAAAAA - AAAAAAA - AAAAAAA -</p>
    <p>AAAAAAA - AAAAAAAA - AAAAAAAAAAA -</p>
    <p>AAAAAAAAAAA - AAAAAAAAAAA -</p>
    <p>AAAAAAAAAAAAAAA - AAAAAAAAAAAAAA</p>
    <p>- AAAAAA AAAAAA - AAAAAAA - AA</p>
    <p>AAAAAAAAAAA - AAAA AAAAAAAAAA -</p>
    <p>AAAAAAAAAAAA - AAAAAAAAA</p>
    <p>AAAAAAAAA AAA- AAAAAAAAA AAAAAAAA</p>
    <p>- AAAAAAAAA</p>
  </section>

  <div class="guitar" role="img" aria-label="Colourful patterned acoustic guitar illustration"></div>

  <div class="date-badge">
    <span>20 TH,</span>
    <span>JULY,</span>
    <span>2019</span>
  </div>

  <div class="ticket-band"></div>
  <p class="tickets">Tickets &amp;<br>Info tellowrasoundcarnival-demo.com</p>

  <footer class="sponsors">SPONSORS</footer>
</div>
</body>
</html>
```